Gently Harbor BC 2019

Hi!
As seen from the attached, I created a 2018 BC that I really like.
It features company details on one side, and a calendar on the other side. The BC is 7" x 2" with a score, so folded it's a regular sized BC.
Company details remain the same, but I need to upgrade and refresh the calendar to 2019. Let your creative juices flow!

The submitted designs so far, while not terrible, most don't take into account that I need a refresher on the current design, but it's a BC that is double sided, and the size of a BC that's side by side wide, with score. (see the attached BC 2018 design). I need the BC to be updated with a 2019 calendar, but essentially because it's such a tiny size, to work the realistic space allocated, and make it readable and striking to stand out and very usable/practical. Let's do this people!

```html
<!DOCTYPE html>
<html lang="en">
<head>
<meta charset="utf-8">
<title>Gently Harbor – 2019 Folded Business Card</title>
<link href="https://fonts.googleapis.com/css2?family=Courier+Prime&family=Kaushan+Script&family=Montserrat:wght@400;500&family=Oswald:wght@500;600&display=swap" rel="stylesheet">
<style>
  :root{
    --stage:#d9d9d9;
    --card:#1b1a1b;
    --ink:#f2f2f2;
    --cyan:#1fb3e5;
    --magenta:#e3177f;
    --yellow:#f5e61a;
    --green:#5cc52b;
    --score:#2b2a2b;
  }
  *{box-sizing:border-box;margin:0;padding:0}
  html,body{width:1200px;height:900px;overflow:hidden;background:var(--stage)}
  body{position:relative;font-family:"Montserrat",sans-serif;color:var(--ink)}
  .card{position:absolute;left:40px;width:1120px;height:320px;background:var(--card);display:flex;box-shadow:0 6px 18px rgba(0,0,0,.18)}
  .card--front{top:100px}
  .card--calendar{top:470px}
  .panel{width:560px;height:100%;position:relative}
  .panel + .panel{border-left:1px solid var(--score)}

  /* front: slogans */
  .slogans{position:absolute;left:70px;top:70px;width:410px}
  .pill{display:block;height:26px;border-radius:13px;margin-bottom:8px;font-family:"Courier Prime",monospace;font-size:17px;line-height:26px;padding-left:22px;letter-spacing:.5px;color:#1b1a1b}
  .pill--cyan{background:var(--cyan)}
  .pill--magenta{background:var(--magenta)}
  .pill--yellow{background:var(--yellow)}
  .motto{font-family:"Kaushan Script",cursive;font-size:26px;margin-top:18px;padding-left:10px}

  /* front: details */
  .brand{position:absolute;right:50px;top:48px;display:flex;align-items:center;gap:12px;font-size:30px;font-weight:400;letter-spacing:1px}
  .brand-mark{width:18px;height:18px;background:var(--magenta)}
  .links{position:absolute;left:40px;top:140px;font-size:15px;list-style:none}
  .links li,.phones li{display:flex;align-items:center;gap:12px;height:26px}
  .phones{position:absolute;right:40px;bottom:40px;font-size:16px;list-style:none;letter-spacing:1px}
  .phones li{justify-content:flex-end}
  .icon{width:18px;height:18px;fill:none;stroke:var(--ink);stroke-width:1.6}

  /* calendar */
  .cal-head{position:absolute;top:14px;left:0;right:0;height:28px;display:flex;align-items:center;justify-content:center}
  .cal-title{font-family:"Kaushan Script",cursive;font-size:20px}
  .cal-year{font-family:"Oswald",sans-serif;font-weight:600;font-size:24px;letter-spacing:2px}
  .cal-grid{position:absolute;top:44px;left:22px;right:22px;display:flex;justify-content:space-between}
  .col{width:160px}
  .month{font-family:"Oswald",sans-serif;font-weight:600;font-size:12px;color:var(--green);letter-spacing:.5px;height:16px;line-height:16px;text-align:center}
  .days{list-style:none;display:grid;grid-template-columns:repeat(7,1fr);grid-auto-rows:13px;height:78px;font-size:10.5px;text-align:center;line-height:13px}
  .days li:first-child{grid-column-start:var(--start)}
  .days .today{color:var(--magenta);font-weight:500}
  .weekdays{list-style:none;display:grid;grid-template-columns:repeat(7,1fr);height:16px;margin:5px 0;font-family:"Oswald",sans-serif;font-weight:500;font-size:8.5px;line-height:16px;text-align:center;color:#1b1a1b}
  .weekdays--cyan{background:var(--cyan)}
  .weekdays--magenta{background:var(--magenta);color:var(--ink)}
  .weekdays--yellow{background:var(--yellow)}
</style>
</head>
<body>

<section class="card card--front" aria-label="Card outside">
  <div class="panel">
    <div class="slogans">
      <span class="pill pill--cyan">Fill your toner with purpose</span>
      <span class="pill pill--magenta">Fill your planet with hope</span>
      <span class="pill pill--yellow">Fill your world with kindness</span>
      <p class="motto">We do good stuff with your stuff</p>
    </div>
  </div>
  <div class="panel">
    <div class="brand"><span class="brand-mark"></span>gentlyharbor.com</div>
    <ul class="links">
      <li><svg class="icon" viewBox="0 0 20 20"><rect x="2" y="4" width="16" height="12"/><path d="M2 4l8 7 8-7"/></svg>pickup@gentlyharbor.com</li>
      <li><svg class="icon" viewBox="0 0 20 20"><rect x="4" y="4" width="12" height="9"/><path d="M1 16h18"/></svg>gentlyharbor.com</li>
    </ul>
    <ul class="phones">
      <li>555.014.2290<svg class="icon" viewBox="0 0 20 20"><path d="M5 2l3 4-2 2c1 2 3 4 5 5l2-2 4 3-2 3C9 17 3 11 2 5z"/></svg></li>
      <li>555.014.7316<svg class="icon" viewBox="0 0 20 20"><path d="M2 4h11v8H7l-3 3v-3H2z"/><path d="M15 8h3v7h-2v2l-2-2h-4"/></svg></li>
      <li>555.014.2291<svg class="icon" viewBox="0 0 20 20"><rect x="3" y="8" width="14" height="9"/><path d="M6 8V3h8v5M6 11h2M10 11h2M6 14h2M10 14h2"/></svg></li>
    </ul>
  </div>
</section>

<section class="card card--calendar" aria-label="2019 calendar">
  <div class="panel">
    <div class="cal-head"><p class="cal-title">Fill Your Day with Purpose</p></div>
    <div class="cal-grid">
      <div class="col">
        <p class="month">JANUARY</p>
        <ol class="days" style="--start:3"><li>1</li><li>2</li><li>3</li><li>4</li><li>5</li><li>6</li><li>7</li><li>8</li><li>9</li><li>10</li><li>11</li><li>12</li><li>13</li><li>14</li><li>15</li><li>16</li><li>17</li><li>18</li><li>19</li><li>20</li><li>21</li><li>22</li><li>23</li><li>24</li><li>25</li><li>26</li><li>27</li><li>28</li><li>29</li><li>30</li><li>31</li></ol>
        <ul class="weekdays weekdays--cyan"><li>SUN</li><li>MON</li><li>TUE</li><li>WED</li><li>THU</li><li>FRI</li><li>SAT</li></ul>
        <ol class="days" style="--start:2"><li>1</li><li>2</li><li>3</li><li>4</li><li>5</li><li>6</li><li>7</li><li>8</li><li>9</li><li>10</li><li>11</li><li>12</li><li>13</li><li>14</li><li>15</li><li>16</li><li>17</li><li>18</li><li>19</li><li>20</li><li>21</li><li>22</li><li>23</li><li>24</li><li>25</li><li>26</li><li>27</li><li>28</li><li>29</li><li>30</li><li>31</li></ol>
        <p class="month">JULY</p>
      </div>
      <div class="col">
        <p class="month">FEBRUARY</p>
        <ol class="days" style="--start:6"><li>1</li><li>2</li><li>3</li><li>4</li><li>5</li><li>6</li><li>7</li><li>8</li><li>9</li><li>10</li><li>11</li><li>12</li><li>13</li><li>14</li><li>15</li><li>16</li><li>17</li><li>18</li><li>19</li><li>20</li><li>21</li><li>22</li><li>23</li><li>24</li><li>25</li><li>26</li><li>27</li><li>28</li></ol>
        <ul class="weekdays weekdays--magenta"><li>SUN</li><li>MON</li><li>TUE</li><li>WED</li><li>THU</li><li>FRI</li><li>SAT</li></ul>
        <ol class="days" style="--start:5"><li>1</li><li>2</li><li>3</li><li>4</li><li>5</li><li>6</li><li>7</li><li>8</li><li>9</li><li>10</li><li>11</li><li>12</li><li>13</li><li>14</li><li>15</li><li>16</li><li>17</li><li>18</li><li>19</li><li>20</li><li>21</li><li>22</li><li>23</li><li>24</li><li>25</li><li>26</li><li>27</li><li>28</li><li>29</li><li>30</li><li>31</li></ol>
        <p class="month">AUGUST</p>
      </div>
      <div class="col">
        <p class="month">MARCH</p>
        <ol class="days" style="--start:6"><li>1</li><li>2</li><li>3</li><li>4</li><li>5</li><li>6</li><li>7</li><li>8</li><li>9</li><li>10</li><li>11</li><li>12</li><li>13</li><li>14</li><li>15</li><li>16</li><li>17</li><li>18</li><li>19</li><li>20</li><li>21</li><li>22</li><li>23</li><li>24</li><li>25</li><li>26</li><li>27</li><li>28</li><li>29</li><li>30</li><li>31</li></ol>
        <ul class="weekdays weekdays--yellow"><li>SUN</li><li>MON</li><li>TUE</li><li>WED</li><li>THU</li><li>FRI</li><li>SAT</li></ul>
        <ol class="days" style="--start:1"><li>1</li><li>2</li><li>3</li><li>4</li><li>5</li><li>6</li><li>7</li><li>8</li><li>9</li><li>10</li><li>11</li><li>12</li><li>13</li><li>14</li><li>15</li><li>16</li><li>17</li><li>18</li><li>19</li><li>20</li><li>21</li><li>22</li><li>23</li><li>24</li><li>25</li><li>26</li><li>27</li><li>28</li><li>29</li><li>30</li></ol>
        <p class="month">SEPTEMBER</p>
      </div>
    </div>
  </div>
  <div class="panel">
    <div class="cal-head"><p class="cal-year">2019</p></div>
    <div class="cal-grid">
      <div class="col">
        <p class="month">APRIL</p>
        <ol class="days" style="--start:2"><li>1</li><li>2</li><li>3</li><li>4</li><li>5</li><li>6</li><li>7</li><li>8</li><li>9</li><li>10</li><li>11</li><li>12</li><li>13</li><li>14</li><li>15</li><li>16</li><li>17</li><li>18</li><li>19</li><li>20</li><li>21</li><li>22</li><li>23</li><li>24</li><li>25</li><li>26</li><li>27</li><li>28</li><li>29</li><li>30</li></ol>
        <ul class="weekdays weekdays--cyan"><li>SUN</li><li>MON</li><li>TUE</li><li>WED</li><li>THU</li><li>FRI</li><li>SAT</li></ul>
        <ol class="days" style="--start:3"><li>1</li><li>2</li><li>3</li><li>4</li><li>5</li><li>6</li><li>7</li><li>8</li><li>9</li><li>10</li><li>11</li><li>12</li><li>13</li><li>14</li><li>15</li><li>16</li><li>17</li><li>18</li><li>19</li><li>20</li><li>21</li><li>22</li><li>23</li><li>24</li><li>25</li><li>26</li><li>27</li><li>28</li><li>29</li><li>30</li><li>31</li></ol>
        <p class="month">OCTOBER</p>
      </div>
      <div class="col">
        <p class="month">MAY</p>
        <ol class="days" style="--start:4"><li>1</li><li>2</li><li>3</li><li>4</li><li>5</li><li>6</li><li>7</li><li>8</li><li>9</li><li>10</li><li>11</li><li>12</li><li>13</li><li>14</li><li>15</li><li>16</li><li>17</li><li>18</li><li>19</li><li>20</li><li>21</li><li>22</li><li>23</li><li>24</li><li>25</li><li>26</li><li>27</li><li>28</li><li>29</li><li>30</li><li>31</li></ol>
        <ul class="weekdays weekdays--magenta"><li>SUN</li><li>MON</li><li>TUE</li><li>WED</li><li>THU</li><li>FRI</li><li>SAT</li></ul>
        <ol class="days" style="--start:6"><li>1</li><li>2</li><li>3</li><li>4</li><li>5</li><li>6</li><li>7</li><li>8</li><li>9</li><li>10</li><li>11</li><li>12</li><li>13</li><li>14</li><li class="today">15</li><li>16</li><li>17</li><li>18</li><li>19</li><li>20</li><li>21</li><li>22</li><li>23</li><li>24</li><li>25</li><li>26</li><li>27</li><li>28</li><li>29</li><li>30</li></ol>
        <p class="month">NOVEMBER</p>
      </div>
      <div class="col">
        <p class="month">JUNE</p>
        <ol class="days" style="--start:7"><li>1</li><li>2</li><li>3</li><li>4</li><li>5</li><li>6</li><li>7</li><li>8</li><li>9</li><li>10</li><li>11</li><li>12</li><li>13</li><li>14</li><li>15</li><li>16</li><li>17</li><li>18</li><li>19</li><li>20</li><li>21</li><li>22</li><li>23</li><li>24</li><li>25</li><li>26</li><li>27</li><li>28</li><li>29</li><li>30</li></ol>
        <ul class="weekdays weekdays--yellow"><li>SUN</li><li>MON</li><li>TUE</li><li>WED</li><li>THU</li><li>FRI</li><li>SAT</li></ul>
        <ol class="days" style="--start:1"><li>1</li><li>2</li><li>3</li><li>4</li><li>5</li><li>6</li><li>7</li><li>8</li><li>9</li><li>10</li><li>11</li><li>12</li><li>13</li><li>14</li><li>15</li><li>16</li><li>17</li><li>18</li><li>19</li><li>20</li><li>21</li><li>22</li><li>23</li><li>24</li><li>25</li><li>26</li><li>27</li><li>28</li><li>29</li><li>30</li><li>31</li></ol>
        <p class="month">DECEMBER</p>
      </div>
    </div>
  </div>
</section>

</body>
</html>
```